Tutoring Website Needs a Facelift

BrightStudyDesk.com needs a facelift! We are looking to completely redo our website, and logo to give it a more professional, cleaner, and younger vibe.
Our site feels out dated and not very Web 2.0
We are looking to keep the same content on the page now but completely rebrand it to give it the new look we desire.
Updates
Target Market(s)
College Students but needs to portray professionalism, and trust to them
Industry/Entity Type
Tutoring
Look and feel
Each slider illustrates characteristics of the customer's brand and the style your logo design should communicate.

```html
<!DOCTYPE html>
<html lang="en">
<head>
<meta charset="utf-8">
<title>BrightStudyDesk.com</title>
<link href="https://fonts.googleapis.com/css2?family=Source+Sans+3:wght@400;600&family=Yanone+Kaffeesatz:wght@700&display=swap" rel="stylesheet">
<style>
:root{
  --brand:#5f9cc0;
  --brand-dark:#4a87ab;
  --heading:#4d88ad;
  --ink:#2b2b2b;
  --muted:#555;
  --arrow:#b5b5b5;
  --footer:#2c2c2c;
  --footer-text:#e6e6e6;
  --white:#fff;
  --s1:#3b5b9c;--s2:#2aa3dc;--s3:#f06a22;--s4:#d8272b;
}
*{margin:0;padding:0;box-sizing:border-box}
html,body{width:1133px;height:1200px;overflow:hidden;background:var(--white)}
body{position:relative;font-family:"Source Sans 3",sans-serif;color:var(--ink)}
.abs{position:absolute}
.logo{left:73px;top:30px;font-size:36px;font-weight:600;color:var(--brand-dark);letter-spacing:-.5px;display:flex;align-items:center;gap:8px}
.logo-mark{width:14px;height:14px;background:var(--brand-dark);border-radius:50%}
.nav{right:10px;top:50px;display:flex;gap:0;font-size:15px;text-transform:uppercase}
.nav a{color:var(--ink);text-decoration:none;padding:7px 19px;line-height:17px}
.nav a.active{background:var(--brand);color:var(--white);padding:7px 16px;margin-right:6px}
.hero{left:0;top:102px;width:1133px;height:484px;background:linear-gradient(180deg,#8fae6a 0%,#6d8f48 40%,#5c6b4a 70%,#7b7460 100%)}
.caption{left:70px;top:389px;width:605px;height:136px;background:rgba(40,40,40,.62);padding:14px 16px;color:var(--white)}
.caption h1{font-family:"Yanone Kaffeesatz",sans-serif;font-size:29px;letter-spacing:.5px;line-height:30px}
.caption h2{font-weight:400;font-size:19px;line-height:24px;margin-top:2px}
.caption p{font-size:13px;line-height:20px;margin-top:5px}
.slider-btn{top:558px;width:21px;height:21px;background:#3a3a3a;display:flex;align-items:center;justify-content:center}
.section-title{font-size:19px;color:var(--heading);text-transform:uppercase;font-weight:400}
.step{width:150px;text-align:center;transform:translateX(-75px)}
.step-label{font-size:18px;color:var(--ink)}
.step-icon{width:78px;height:78px;border-radius:50%;background:var(--brand);margin:6px auto 9px;display:flex;align-items:center;justify-content:center}
.step-text{font-size:13px;line-height:17px;color:var(--ink);width:128px;margin:0 auto}
.step-arrow{top:700px}
.photo{display:block}
.lead{font-size:14.5px;line-height:21px;color:var(--ink)}
.body-text{font-size:11.5px;line-height:19.5px;color:var(--muted)}
.footer{left:0;top:1118px;width:1133px;height:82px;background:var(--footer);color:var(--footer-text);font-size:11.5px}
.social{top:26px;width:30px;height:30px}
</style>
</head>
<body>

<header>
  <div class="abs logo"><span>BrightStudyDesk.com</span><span class="logo-mark"></span></div>
  <nav class="abs nav">
    <a class="active" href="#">Home</a><a href="#">Submission Form</a><a href="#">Testimonials</a><a href="#">FAQ</a><a href="#">Contact</a>
  </nav>
</header>

<section class="abs hero" role="img" aria-label="Photo of a group of college students chatting outdoors on a campus lawn"></section>
<div class="abs caption">
  <h1>DESIGNED BY COLLEGE STUDENTS FOR COLLEGE STUDENTS</h1>
  <h2>LOREM IPSUM DOLOR SIT AMET, CONSECTETUER ADIPISCING ELIT</h2>
  <p>Jerta baditaut onsequser untur magni dolores eoquie voluptate msequi nesciunt. Voluptatem accusant ium dolorem. Ut wisi enim ad minim veniam, quis nostrud exerci tation ullamcorper suscipit lobortis.</p>
</div>
<div class="abs slider-btn" style="left:1012px"><svg width="10" height="12"><path d="M7 1 2 6l5 5" stroke="#fff" stroke-width="2" fill="none"/></svg></div>
<div class="abs slider-btn" style="left:1040px"><svg width="10" height="12"><path d="M3 1l5 5-5 5" stroke="#fff" stroke-width="2" fill="none"/></svg></div>

<h2 class="abs section-title" style="left:68px;top:607px">How it works?</h2>

<div class="abs step" style="left:131px;top:662px">
  <div class="step-label">STEP 1</div>
  <div class="step-icon"><svg width="40" height="40" viewBox="0 0 40 40" fill="none" stroke="#fff" stroke-width="2"><path d="M9 4h15l7 7v25H9z"/><path d="M13 14h12M13 19h12M13 24h8"/><circle cx="28" cy="29" r="6" fill="var(--brand)"/><path d="M28 27v5M28 25v.5"/></svg></div>
  <div class="step-text">Complete Submission Form</div>
</div>
<div class="abs step" style="left:317px;top:662px">
  <div class="step-label">STEP 2</div>
  <div class="step-icon"><svg width="44" height="40" viewBox="0 0 44 40" fill="#fff"><path d="M22 6 40 15 22 24 4 15z"/><path d="M4 21l18 9 18-9" fill="none" stroke="#fff" stroke-width="2.5"/><path d="M4 27l18 9 18-9" fill="none" stroke="#fff" stroke-width="2.5"/></svg></div>
  <div class="step-text">Assignment is reviewed by brightstudydesk.com</div>
</div>
<div class="abs step" style="left:496px;top:662px">
  <div class="step-label">STEP 3</div>
  <div class="step-icon"><svg width="44" height="44" viewBox="0 0 44 44" fill="none" stroke="#fff"><circle cx="17" cy="27" r="9" stroke-width="6" stroke-dasharray="4 3"/><circle cx="17" cy="27" r="5" stroke-width="3"/><circle cx="31" cy="12" r="5" stroke-width="4" stroke-dasharray="3 2"/></svg></div>
  <div class="step-text">You will receive a confirmation email verifying the assignment.</div>
</div>
<div class="abs step" style="left:675px;top:662px">
  <div class="step-label">STEP 4</div>
  <div class="step-icon"><svg width="44" height="44" viewBox="0 0 44 44" fill="none" stroke="#fff" stroke-width="3" stroke-linecap="round"><path d="M9 35 35 9"/><path d="M9 9l26 26"/><circle cx="11" cy="11" r="4"/><circle cx="33" cy="33" r="4"/></svg></div>
  <div class="step-text">You will receive a confirmation email verifying the assignment.</div>
</div>
<div class="abs step" style="left:838px;top:662px">
  <div class="step-label">STEP 5</div>
  <div class="step-icon"><svg width="44" height="44" viewBox="0 0 44 44" fill="none" stroke="#fff" stroke-width="2.5" stroke-linejoin="round"><path d="M38 6 6 22l12 4 4 12z"/><path d="M38 6 18 26"/></svg></div>
  <div class="step-text">Your party starts</div>
</div>
<div class="abs step" style="left:1003px;top:662px">
  <div class="step-label">STEP 6</div>
  <div class="step-icon"><svg width="44" height="44" viewBox="0 0 44 44" fill="none" stroke="#fff" stroke-width="2.5" stroke-linejoin="round"><path d="M14 10h18v26H14z"/><path d="M14 10 9 14v22l5-0"/><path d="M19 16h8M19 21h8M19 26h6"/></svg></div>
  <div class="step-text">Payment is due within 24 hours. Your work will not be started untill payment is received</div>
</div>

<svg class="abs step-arrow" style="left:219px" width="16" height="48"><path d="M3 2l10 22-10 22" stroke="var(--arrow)" stroke-width="2" fill="none"/></svg>
<svg class="abs step-arrow" style="left:399px" width="16" height="48"><path d="M3 2l10 22-10 22" stroke="var(--arrow)" stroke-width="2" fill="none"/></svg>
<svg class="abs step-arrow" style="left:578px" width="16" height="48"><path d="M3 2l10 22-10 22" stroke="var(--arrow)" stroke-width="2" fill="none"/></svg>
<svg class="abs step-arrow" style="left:753px" width="16" height="48"><path d="M3 2l10 22-10 22" stroke="var(--arrow)" stroke-width="2" fill="none"/></svg>
<svg class="abs step-arrow" style="left:908px" width="16" height="48"><path d="M3 2l10 22-10 22" stroke="var(--arrow)" stroke-width="2" fill="none"/></svg>

<h2 class="abs section-title" style="left:69px;top:874px">Welcome to our website</h2>
<div class="abs photo" style="left:68px;top:915px;width:268px;height:167px;background:radial-gradient(ellipse at 45% 15%,#e8dcc0 0%,#8a7a5c 30%,#2a241c 70%,#141210 100%)" role="img" aria-label="Photo of a concert crowd with raised hands under stage lights"></div>
<p class="abs lead" style="left:361px;top:907px;width:350px">Ut wisi enim ad minim veniam, quis nostrud exerci tation ulli amcorper suscipit lobortis nisl ut aliquip exea.</p>
<p class="abs body-text" style="left:361px;top:956px;width:340px">Incididunt ut labore et dolore magna aliqua. Ut enim ad minim veniam, quis nostrud exercitation ullamcolaboris nisi ut aliquip ex ea commodo consequat. Duis tefd aute iruredolor inreprehenderit in voluptate velit esse cillum.Dolore magna aliqua. Ut enim ad minim veniam, Quisnostru dexercitation ullamco laboris nisi ut aliquip. Ut enim ad minim veniam, quis nostrud exercitation ullamco laboris. Claritas est etiam processus dynamicus, qui sequitur mutationem.</p>

<h2 class="abs section-title" style="left:763px;top:874px">What we do?</h2>
<div class="abs photo" style="left:765px;top:913px;width:297px;height:124px;background:linear-gradient(180deg,#7f9a5a 0%,#6c8449 45%,#3e5a86 75%,#c9764a 100%)" role="img" aria-label="Photo of five smiling students standing together on grass"></div>
<p class="abs body-text" style="left:765px;top:1051px;width:300px;font-size:11px;line-height:18px">Claritas est etiam processus dynamicus, qui sequitur mutationem consuetudium lectorum. Mirum est notare quam littera.</p>

<footer class="abs footer">
  <div class="abs" style="left:69px;top:21px">Home | Submission Form | Testimonials | FAQ | Contact</div>
  <div class="abs" style="left:69px;top:48px">Copyrights 2013. All Rights Reserved.</div>
  <div class="abs social" style="left:919px;background:var(--s1)" role="img" aria-label="Friendsy"></div>
  <div class="abs social" style="left:958px;background:var(--s2)" role="img" aria-label="Chirply"></div>
  <div class="abs social" style="left:996px;background:var(--s3)" role="img" aria-label="FeedLoop"></div>
  <div class="abs social" style="left:1034px;background:var(--s4)" role="img" aria-label="ClipCast"></div>
</footer>

</body>
</html>
```